Stylish Business Card for Modern hair salon

I need a simple business card design using our salon logo and colours that are in the logo. We service clients of all ages but predominantly those in the 18 to 55 age range. We have a young staff and are looking to have a card that will present a modern and clean image that represents who we are. The card should be in black and white same as our logo. Minimal use of other colours is allowed.

Industry/Entity Type

Hair And Beauty

Contact Information for Business Card

The design should have the following information
salon name - TR Hair Studio
address - 2751 Birchfield Rd.E. Mississauga, ON L7P3K2
phone - 905 614-2870
website - trhairexample.ca
instagram - tr.hairstudio
twitter - @TR_HairStudio

Colors
000000
ffffff
474747

Requirements
Must have
• simple design, salon name, address, phone, website, instagram, twitter info
• Back of card should have the following:
• YOUR NEXT APPOINTMENT
• DATE
• TIME
Nice to have
• simple design, clear to see and read,
• predominantly black and white colour, minimal use of other colours is ok
Should not have
• many colours, various fonts

```html
<!DOCTYPE html>
<html lang="en">
<head>
<meta charset="utf-8">
<title>TR Hair Studio – Business Card</title>
<link rel="stylesheet" href="https://fonts.googleapis.com/css2?family=Tinos&display=swap">
<style>
  :root {
    --ink: #000000;
    --paper: #ffffff;
    --charcoal: #474747;
    --card-back: #262626;
    --stage: #ebe9ea;
    --text-dark: #1a1a1a;
  }
  * { margin: 0; padding: 0; box-sizing: border-box; }
  html, body {
    width: 1200px; height: 1000px; overflow: hidden;
    background: var(--stage);
    font-family: "Tinos", "Times New Roman", serif;
  }
  .canvas { position: relative; width: 1200px; height: 1000px; }

  .card { position: absolute; left: 251px; width: 676px; height: 385px; }
  .card--front { top: 96px; background: var(--paper); color: var(--text-dark); }
  .card--back { top: 519px; background: var(--card-back); color: var(--paper); }

  .card__frame { position: absolute; left: 24px; top: 24px; width: 629px; height: 338px; }
  .card--front .card__frame { border: 2px solid var(--ink); }
  .card--back .card__frame { border: 1.5px solid var(--paper); }

  .brand-name {
    position: absolute; left: 94px; top: 167px; width: 200px;
    text-align: center; font-size: 30px; line-height: 1; color: var(--ink);
  }

  .divider { position: absolute; left: 338px; top: 116px; width: 1.5px; height: 156px; background: var(--ink); }

  .studio-title { position: absolute; left: 382px; top: 110px; font-size: 21px; font-weight: 400; letter-spacing: 0.5px; color: var(--ink); }

  .contact-list { position: absolute; left: 376px; top: 149px; list-style: none; }
  .contact-list li {
    display: flex; align-items: center; height: 24.5px;
    font-size: 15.5px; letter-spacing: 1px; color: var(--charcoal);
  }
  .contact-list .icon { width: 16px; height: 16px; margin-right: 17px; flex: none; }

  .address { position: absolute; left: 376px; top: 234px; font-size: 15.5px; font-style: normal; line-height: 22px; letter-spacing: 1px; color: var(--charcoal); }

  .website {
    position: absolute; left: 0; top: 350px; width: 100%;
    text-align: center; line-height: 22px;
  }
  .website__text {
    display: inline-block; padding: 0 10px; background: var(--paper);
    font-size: 15.5px; letter-spacing: 1px; color: var(--charcoal);
  }

  .appointment-title {
    position: absolute; left: 0; width: 100%; top: 84px; text-align: center;
    font-size: 21px; font-weight: 400; letter-spacing: 2px;
  }
  .appointment-fields { position: absolute; left: 96px; top: 193px; width: 480px; }
  .field-line {
    display: flex; align-items: flex-end; height: 27px;
    font-size: 14.5px; letter-spacing: 1.5px;
  }
  .field-line .label { margin-right: 6px; }
  .field-line .rule { flex: 1; border-bottom: 1.5px dotted var(--paper); margin-bottom: 3px; }
</style>
</head>
<body>
<main class="canvas">

  <section class="card card--front" aria-label="Business card front">
    <div class="card__frame"></div>

    <div class="brand-name">TR Hair Studio</div>

    <div class="divider"></div>

    <h1 class="studio-title">TR HAIR STUDIO</h1>

    <ul class="contact-list">
      <li>
        <svg class="icon" viewBox="0 0 16 16" aria-hidden="true">
          <rect x="4" y="1.5" width="8" height="13" rx="1.2" fill="none" stroke="#1a1a1a" stroke-width="1.4"/>
          <line x1="7" y1="12.3" x2="9" y2="12.3" stroke="#1a1a1a" stroke-width="1.2"/>
        </svg>
        905 614-2870
      </li>
      <li>
        <svg class="icon" viewBox="0 0 16 16" aria-hidden="true">
          <circle cx="8" cy="8" r="5.5" fill="none" stroke="#1a1a1a" stroke-width="1.4"/>
        </svg>
        tr.hairstudio
      </li>
      <li>
        <svg class="icon" viewBox="0 0 16 16" aria-hidden="true">
          <circle cx="8" cy="8" r="5.5" fill="#1a1a1a"/>
        </svg>
        @TR_HairStudio
      </li>
    </ul>

    <address class="address">
      2751 Birchfield Rd.E.<br>
      Mississauga, ON L7P3K2
    </address>

    <div class="website"><span class="website__text">www.trhairexample.ca</span></div>
  </section>

  <section class="card card--back" aria-label="Business card back">
    <div class="card__frame"></div>

    <h2 class="appointment-title">YOUR NEXT APPOINTMENT</h2>

    <div class="appointment-fields">
      <div class="field-line"><span class="label">DATE</span><span class="rule"></span></div>
      <div class="field-line"><span class="rule"></span></div>
      <div class="field-line"><span class="label">TIME</span><span class="rule"></span></div>
      <div class="field-line"><span class="rule"></span></div>
    </div>
  </section>

</main>
</body>
</html>
```